An internal sign in a physiotherapy clinic with gym. About working hard

We are a physiotherapy clinic / gym and we are wanting an internal wall to be a large sign with a great slogan
We are after 3 parts to it
1. The image / backdrop
2. The slogan
3. Our clinic logo

I have attached some images of the concept of what we are after. It can be climbing a mountain, rockclimbing and even hard work in a gym.

The slogan is:
"IF IT DOESN'T CHALLENGE YOU, IT WON'T CHANGE YOU"

Logo
I have attached a few different versions of our logo to assist you in the sign based on the background

THE SIGN SIZE WILL BE:
2935mm wide x 1885mm high

```html
<!DOCTYPE html>
<html lang="en">
<head>
<meta charset="utf-8">
<title>Hartfield Sports Medicine – Challenge Wall Sign</title>
<link rel="stylesheet" href="https://fonts.googleapis.com/css2?family=Oswald:wght@600&display=swap">
<style>
  :root {
    --page-bg: #e4e4e4;
    --navy: #151c44;
    --orange-deep: #d2431a;
    --orange: #f57a0c;
    --amber: #fdb800;
    --yellow: #fde80d;
    --pale-yellow: #f8ea7a;
    --white: #ffffff;
    --sky: #3fc1ec;
  }
  * { margin: 0; padding: 0; box-sizing: border-box; }
  html, body {
    width: 1200px;
    height: 1000px;
    overflow: hidden;
    background: var(--page-bg);
  }
  .wall-sign {
    position: absolute;
    left: 40px;
    top: 140px;
    width: 1122px;
    height: 720px;
    overflow: hidden;
    background: linear-gradient(140deg,
      var(--orange-deep) 0%,
      var(--orange) 42%,
      var(--amber) 66%,
      var(--yellow) 80%,
      var(--pale-yellow) 100%);
  }
  .climber-artwork {
    position: absolute;
    left: 250px;
    top: 0;
    width: 872px;
    height: 580px;
    background: linear-gradient(100deg,
      rgba(21, 28, 68, 0) 0%,
      rgba(21, 28, 68, 0.45) 30%,
      rgba(21, 28, 68, 0.85) 60%,
      var(--navy) 80%);
    border-bottom-left-radius: 60% 40%;
  }
  .clinic-name {
    position: absolute;
    left: 735px;
    top: 44px;
    display: flex;
    align-items: center;
    gap: 16px;
    font-family: 'Oswald', sans-serif;
    font-weight: 600;
    color: var(--white);
    text-transform: uppercase;
  }
  .clinic-name__dot {
    width: 20px;
    height: 20px;
    border-radius: 50%;
    background: var(--sky);
    flex: none;
  }
  .clinic-name__text {
    display: flex;
    flex-direction: column;
    line-height: 1;
  }
  .clinic-name__primary {
    font-size: 40px;
    letter-spacing: 2px;
  }
  .clinic-name__secondary {
    font-size: 17px;
    letter-spacing: 6.4px;
    margin-top: 6px;
  }
  .slogan {
    position: absolute;
    left: 63px;
    top: 388px;
    font-family: 'Oswald', sans-serif;
    font-weight: 600;
    font-size: 58px;
    line-height: 63px;
    color: var(--white);
    text-transform: uppercase;
    letter-spacing: 0.5px;
    text-shadow: 3px 4px 6px rgba(90, 30, 0, 0.55);
  }
  .slogan span { display: block; }
</style>
</head>
<body>
  <main class="wall-sign">
    <div class="climber-artwork" role="img" aria-label="Navy silhouette of a rock climber on a rope hanging from a cliff face on the right"></div>

    <div class="clinic-name">
      <span class="clinic-name__dot"></span>
      <div class="clinic-name__text">
        <span class="clinic-name__primary">Hartfield</span>
        <span class="clinic-name__secondary">Sports Medicine</span>
      </div>
    </div>

    <h1 class="slogan">
      <span>If it doesn't</span>
      <span>challenge you</span>
      <span>it won't</span>
      <span>change you</span>
    </h1>
  </main>
</body>
</html>
```